Pemberton Dialworks Business Card Design

Double Sided Business Card Design for a Locksmith company specializing in Safecracking, safe & vault service.

```html
<!DOCTYPE html>
<html lang="en">
<head>
<meta charset="utf-8">
<title>Pemberton Dialworks Business Card</title>
<link href="https://fonts.googleapis.com/css2?family=Montserrat:wght@600;700&family=Questrial&display=swap" rel="stylesheet">
<style>
  :root {
    --page: #8a9ba0;
    --card: #2b2d31;
    --card-deep: #25272b;
    --green: #3f9b62;
    --green-deep: #2f7c4d;
    --white: #ffffff;
    --soft: #e8ecea;
  }
  * { box-sizing: border-box; margin: 0; padding: 0; }
  html, body {
    width: 1200px; height: 900px; overflow: hidden;
    background: var(--page);
    font-family: "Questrial", sans-serif;
  }
  .canvas {
    width: 1200px; height: 900px;
    display: flex; flex-direction: column;
    align-items: center; justify-content: center; gap: 40px;
  }
  .card {
    position: relative;
    width: 600px; height: 343px;
    border-radius: 26px;
    background: var(--card);
    overflow: hidden;
  }
  .card-art { position: absolute; inset: 0; width: 100%; height: 100%; }
  .tagline, .web {
    font-family: "Questrial", sans-serif;
    fill: var(--white);
    font-size: 15px;
    letter-spacing: 0.4px;
  }

  /* Front */
  .brand {
    position: absolute;
    display: flex; align-items: center; gap: 10px;
  }
  .brand-mark {
    width: 26px; height: 26px; border-radius: 50%;
    background: var(--green); flex: none;
  }
  .brand-name {
    font-family: "Montserrat", sans-serif;
    font-weight: 700;
    color: var(--white);
    font-size: 19px; line-height: 1.1;
    text-transform: uppercase;
    letter-spacing: 0.5px;
  }
  .front .brand { left: 56px; top: 124px; }
  .divider {
    position: absolute; left: 300px; top: 70px;
    width: 2px; height: 140px; background: var(--green);
  }
  .person { position: absolute; left: 326px; top: 68px; }
  .person-name {
    font-family: "Montserrat", sans-serif; font-weight: 600;
    color: var(--green); font-size: 19px;
  }
  .person-role { color: var(--soft); font-size: 16px; margin-top: 2px; }
  .contacts { list-style: none; margin-top: 18px; }
  .contacts li {
    display: flex; align-items: center; gap: 10px;
    color: var(--soft); font-size: 15px; margin-bottom: 9px;
  }
  .contacts svg { width: 16px; height: 16px; flex: none; }

  /* Back */
  .back .brand { left: 50%; top: 128px; transform: translateX(-50%); }
</style>
</head>
<body>
<main class="canvas">

  <section class="card front" aria-label="Card front">
    <svg class="card-art" viewBox="0 0 600 343" aria-hidden="true">
      <path d="M0,343 L0,322 C180,290 400,262 600,206 L600,343 Z" fill="var(--green)"/>
      <path d="M0,316 C180,284 400,256 600,200" fill="none" stroke="var(--white)" stroke-width="2"/>
      <path id="front-curve" d="M40,326 C200,298 400,270 600,222" fill="none"/>
      <text class="tagline"><textPath href="#front-curve" startOffset="6%">specializing in Safecracking, safe &amp; vault service</textPath></text>
    </svg>

    <div class="brand">
      <span class="brand-mark"></span>
      <span class="brand-name">Pemberton<br>Dialworks</span>
    </div>

    <div class="divider"></div>

    <div class="person">
      <p class="person-name">Your name here</p>
      <p class="person-role">Vice President</p>
      <ul class="contacts">
        <li>
          <svg viewBox="0 0 16 16" aria-hidden="true"><circle cx="8" cy="8" r="7" fill="none" stroke="var(--green)" stroke-width="1.2"/><path d="M5.5,4.5 L7,6 L6.2,7 C6.8,8.2 7.8,9.2 9,9.8 L10,9 L11.5,10.5 L10.5,11.5 C7.5,11 5,8.5 4.5,5.5 Z" fill="var(--green)"/></svg>
          555-218-4073
        </li>
        <li>
          <svg viewBox="0 0 16 16" aria-hidden="true"><circle cx="8" cy="8" r="7" fill="none" stroke="var(--green)" stroke-width="1.2"/><rect x="5" y="4" width="6" height="3" fill="none" stroke="var(--green)" stroke-width="1"/><rect x="4" y="7" width="8" height="4" fill="none" stroke="var(--green)" stroke-width="1"/></svg>
          555-218-4091
        </li>
        <li>
          <svg viewBox="0 0 16 16" aria-hidden="true"><circle cx="8" cy="8" r="7" fill="none" stroke="var(--green)" stroke-width="1.2"/><circle cx="8" cy="8" r="2" fill="none" stroke="var(--green)" stroke-width="1.1"/><path d="M10,6 L10,9 C10,10.5 12,10.5 12,8.5 C12,6 10.2,4.2 8,4.2 C5.8,4.2 4,6 4,8 C4,10.2 5.8,12 8,12" fill="none" stroke="var(--green)" stroke-width="1.1"/></svg>
          you@pdialworks.com
        </li>
      </ul>
    </div>
  </section>

  <section class="card back" aria-label="Card back">
    <svg class="card-art" viewBox="0 0 600 343">
      <defs>
        <radialGradient id="pattern-tone" cx="50%" cy="45%" r="70%">
          <stop offset="0%" stop-color="#2f3a33"/>
          <stop offset="100%" stop-color="var(--card-deep)"/>
        </radialGradient>
      </defs>
      <rect width="600" height="343" fill="url(#pattern-tone)" role="img" aria-label="Repeating pattern of faint green combination dials"/>
      <path d="M0,343 L0,322 C180,290 400,262 600,206 L600,343 Z" fill="var(--green)"/>
      <path d="M0,316 C180,284 400,256 600,200" fill="none" stroke="var(--white)" stroke-width="2"/>
      <path id="back-curve" d="M40,326 C200,298 400,270 600,222" fill="none"/>
      <text class="web"><textPath href="#back-curve" startOffset="58%">www.pdialworks.com</textPath></text>
    </svg>

    <div class="brand">
      <span class="brand-mark"></span>
      <span class="brand-name">Pemberton<br>Dialworks</span>
    </div>
  </section>

</main>
</body>
</html>
```